Consulting Firm stationery design

Now that the ArtHive has given us a new logo we'll now need to have all our stationery designed. So we're asking for this community to help us once again.We're looking to get from you Letterheads (Header and Footer, suitable to be applied on a .docx format. Vectors are required but keep this in mind), Envelopes (Front and Back designs, back is not a must but desirable depending on your design), 9"x 12" Pocket Folders (consider design for front and back, also for pockets as well), Business Cards.An elegant design is a must have, mostly for Folders and Envelopes. The idea with this two is to stand out from others when they're handed over. Ideas are welcomed, we were thinking maybe on some texturing simulation for these.Folders will have 3 addresses and contact information. Envelopes will have 1 address and contact information.Brand Manual attached. marquesino logo has been copyrighted already. I'm also attaching the current stationary designs (these never got to be out for production but was going to be before we made the brand changes); Pocker folders page 1 to 4 (pages 2 and 4 are the pocket designs), Pages 5 and 6 (6 is the back of the envelope), Pages 7 and 8 (8 is the back of the business card). No letterhead within these designs as it just had the logo and address.

Industry/Entity Type

Business Consultant

Font styles to use
Serif
Sans Serif

Requirements
Must have
• Elegance
Nice to have
• Modern looking out of common

```html
<!DOCTYPE html>
<html lang="en">
<head>
<meta charset="utf-8">
<title>Marquesino Stationery</title>
<link href="https://fonts.googleapis.com/css2?family=Questrial&family=Tinos&display=swap" rel="stylesheet">
<style>
:root{
  --bg:#e9e9ea;
  --paper:#f7f7f7;
  --navy:#2f323d;
  --blue:#0a7bb8;
  --ink:#3a3c44;
  --letter:#2b2b2b;
}
*{margin:0;padding:0;box-sizing:border-box}
html,body{width:1200px;height:1091px;overflow:hidden;background:var(--bg)}
body{position:relative;font-family:"Questrial",sans-serif;color:var(--ink)}
.sheet{position:absolute;background:var(--paper);overflow:hidden}
.brand{position:absolute;font-family:"Questrial",sans-serif;color:var(--navy);line-height:1;white-space:nowrap;display:flex;align-items:center;gap:.22em}
.brand .dot{display:inline-block;width:.3em;height:.3em;border-radius:50%;background:var(--blue)}
.brand.light{color:#fff}

/* envelope back */
.envelope-back{left:98px;top:131px;width:415px;height:208px}
.envelope-back .flap{position:absolute;left:0;top:0;width:100%;height:66px;background:var(--navy);border-bottom-left-radius:26px}
.envelope-back .brand{left:178px;top:15px;font-size:15px}

/* envelope front & footer */
.envelope-front{left:195px;top:168px;width:417px;height:209px;background:#fbfbfb}
.envelope-front .brand{left:28px;top:22px;font-size:20px}
.contact{position:absolute;display:flex;gap:14px;font-size:5.6px;line-height:7.4px;color:var(--ink)}
.contact .company{font-size:7.4px;letter-spacing:1.3px;color:var(--blue);line-height:9px}
.envelope-front .contact{left:28px;top:159px}
.bars{position:absolute;display:flex;gap:3px;height:11px}
.bars .band{background:var(--navy);border-top-left-radius:9px}
.bars .accent{background:var(--blue)}
.envelope-front .bars{left:184px;bottom:0}
.envelope-front .band{width:183px}
.envelope-front .accent{width:46px}

/* letterhead */
.letterhead{left:218px;top:441px;width:397px;height:561px}
.letterhead .brand{right:40px;top:40px;font-size:20px}
.letter{position:absolute;left:47px;top:84px;width:304px;font-family:"Tinos",serif;font-size:8.1px;line-height:9.6px;color:var(--letter)}
.letter p{margin-bottom:9px}
.letter .gap{margin-bottom:19px}
.letterhead .contact{left:47px;top:514px}
.letterhead .bars{left:184px;bottom:0}
.letterhead .band{width:159px}
.letterhead .accent{width:51px}

/* folder */
.folder{left:669px;top:131px;width:436px;height:596px;background:var(--navy)}
.folder .brand{right:44px;top:520px;font-size:30px}
.folder .accent{position:absolute;right:0;top:506px;width:28px;height:59px;background:var(--blue)}

/* business cards */
.card{top:916px;width:171px;height:85px}
.card-front{left:747px;background:var(--navy)}
.card-front .brand{right:16px;top:56px;font-size:11px}
.card-front .accent{position:absolute;right:0;top:51px;width:8px;height:25px;background:var(--blue)}
.card-back{left:934px;background:#fbfbfb}
.card-back .brand{right:15px;top:14px;font-size:11px}
.card-back .accent{position:absolute;right:0;top:8px;width:8px;height:25px;background:var(--blue)}
.card-details{position:absolute;left:22px;top:40px;width:140px;font-size:3.6px;line-height:4.6px;color:var(--ink)}
.card-details .name{font-size:5.2px;color:var(--blue);line-height:6px}
.card-details .name span{color:var(--ink);font-size:3.6px}
.card-details .block{margin-top:4px}
</style>
</head>
<body>

<section class="sheet envelope-back" aria-label="Envelope back">
  <div class="flap"></div>
  <div class="brand light">marquesino<span class="dot"></span></div>
</section>

<section class="sheet envelope-front" aria-label="Envelope front">
  <div class="brand">marquesino<span class="dot"></span></div>
  <div class="contact">
    <div>
      <div class="company">MARQUESINO SRL</div>
      Ceiba Business Tower<br>Av. Las Palmas 42, Naco<br>Santo Domingo, Rep. Dominicana
    </div>
    <div style="padding-top:9px">
      Tel: (809) 555 0142 ext. 201<br>M (809) 555 0177<br>E elena@marquesino.do
    </div>
  </div>
  <div class="bars"><div class="band"></div><div class="accent"></div></div>
</section>

<section class="sheet letterhead" aria-label="Letterhead">
  <div class="brand">marquesino<span class="dot"></span></div>
  <div class="letter">
    <p>Queens, NY 11375</p>
    <p class="gap">June 28, 2007</p>
    <p class="gap">Ms. Clara Whitfield<br>Harbor Light Fellowship<br>&nbsp;&nbsp;40 Linden Avenue<br>New York, NY 10024</p>
    <p>Dear Ms. Whitfield:</p>
    <p class="gap">The Harbor Light Fellowship has always loomed on the horizon for me. Ever since I decided to major in history, I have wanted to participate in your program. From the research that I have done, I believe that your program provides its participants with an extensively detailed look at the history of the world through hands-on experience with fossils, artifacts, and other remains that compose the blueprint of our existence. I am applying for the Harbor Light Fellowship because I believe that it would benefit me throughout my career and allow me to further understand the ideas behind history and how it is constructed.</p>
    <p>I believe my skills, experience, and goals make me an excellent candidate for your program.</p>
    <p class="gap">Thank you very much for considering me for the Harbor Light Fellowship. I am looking forward to hearing from you.</p>
    <p>Sincerely,</p>
    <p>&nbsp;&nbsp;&nbsp;&nbsp;&nbsp;&nbsp;&nbsp;Mara<br>(419) 555-0188</p>
  </div>
  <div class="contact">
    <div>
      <div class="company">MARQUESINO SRL</div>
      Ceiba Business Tower<br>Av. Las Palmas 42, Naco<br>Santo Domingo, Rep. Dominicana
    </div>
    <div style="padding-top:9px">
      T (809) 555 0142 ext. 201<br>M (809) 555 0177<br>E elena@marquesino.do
    </div>
  </div>
  <div class="bars"><div class="band"></div><div class="accent"></div></div>
</section>

<section class="sheet folder" aria-label="Pocket folder cover">
  <div class="brand light">marquesino<span class="dot"></span></div>
  <div class="accent"></div>
</section>

<section class="sheet card card-front" aria-label="Business card front">
  <div class="brand light">marquesino<span class="dot"></span></div>
  <div class="accent"></div>
</section>

<section class="sheet card card-back" aria-label="Business card back">
  <div class="brand">marquesino<span class="dot"></span></div>
  <div class="accent"></div>
  <div class="card-details">
    <div class="name">Elena M. Rivas <span>| COO &amp; Partner</span></div>
    <div>Certified Auditor, Data Analytics Lead</div>
    <div class="block">MARQUESINO SRL<br>Ceiba Business Tower Av. Las Palmas 42, Naco Santo Domingo, Rep. Dominicana<br>D (809) 555 0142 ext. 201 &nbsp;&nbsp; M (809) 555 0177 &nbsp;&nbsp; E elena@marquesino.do</div>
  </div>
</section>

</body>
</html>
```